New letterhead/ stationary design for insurance restoration builder

Modern, clever creative not cheap tacky design maroon and black / white are logo colours. Company name is Harbor Peak Building Services. Might need two different versions of new design, one for standard letterhead communicatio, the other i need to use for management aystems policies amd procedirrs etc.becauuse you wong have tome
Target Market(s)
Large residential insurance companies and their clients, tradespeople and the integrated management system with policies and procedures is internal company employees.
Font styles to use
Requirements
Must have
- A version that would be used as a typical business letterhead is and the other needs to be in a format / design that suits company policies and procedures. Be professional, HARBOR PEAK and be creative / totally custom for pur business not just an edited version of what you can get for free in Word or off the internet pls. Incorporating industry relevant shapes or placement to create the illusion of a residential construction related image is an idea. Someone who is cleverly creative with simple but impactdul design will get my interest.
Nice to have
- Can have different shades of the corporate colours used which are maroon / burgundy and black. https://fernlowmedia.example/common/images/v3/sketch-icon-dropzone.png
Should not have
- Look like the genetic templates and designs you can do yourself copying off the internet.

```html
<!DOCTYPE html>
<html lang="en">
<head>
<meta charset="utf-8">
<title>Harbor Peak Building Services – Letterhead</title>
<link href="https://fonts.googleapis.com/css2?family=Open+Sans:wght@400;600;700&family=Arimo:wght@400&family=Lato:wght@400&display=swap" rel="stylesheet">
<style>
  :root {
    --maroon: #a3063f;
    --accent: #d2104f;
    --ink: #3c3c3c;
    --black: #000000;
    --paper: #ffffff;
  }
  * { margin: 0; padding: 0; box-sizing: border-box; }
  html, body { width: 1040px; height: 1200px; overflow: hidden; background: var(--paper); }
  .letterhead {
    position: relative; width: 1040px; height: 1200px;
    background: var(--paper); font-family: "Open Sans", sans-serif; color: var(--ink);
  }
  .top-band { position: absolute; top: 0; left: 0; width: 100%; height: 15px; background: var(--maroon); }
  .brand {
    position: absolute; top: 62px; left: 0; width: 100%;
    display: flex; justify-content: center; align-items: center; gap: 12px;
  }
  .brand-square { width: 22px; height: 22px; background: var(--maroon); }
  .brand-name {
    font-weight: 700; font-size: 26px; color: var(--maroon);
    letter-spacing: 0.5px;
  }
  .letter-body { position: absolute; left: 98px; width: 842px; font-size: 15.5px; }
  .issue-date { top: 212px; }
  .recipient { top: 250px; line-height: 20px; }
  .salutation { top: 354px; }
  .paragraphs { top: 408px; line-height: 27px; text-align: justify; }
  .paragraphs p { margin-bottom: 27px; }
  .closing { top: 812px; }
  .signatory { top: 888px; }
  .signatory-name { font-size: 19px; font-weight: 600; color: #333; }
  .signatory-role { margin-top: 4px; }
  .footer {
    position: absolute; left: 0; bottom: 0; width: 100%; height: 77px;
    background: var(--black); color: #fff; text-align: center;
  }
  .footer-address { font-family: "Lato", sans-serif; font-size: 18px; padding-top: 9px; }
  .footer-rule { width: 720px; height: 1px; background: #333; margin: 7px auto 4px; }
  .footer-contacts { font-family: "Arimo", sans-serif; font-size: 18px; }
  .footer-contacts .label, .footer-contacts .highlight { color: var(--accent); }
  .footer-contacts .sep { margin: 0 8px; }
</style>
</head>
<body>
<div class="letterhead">
  <div class="top-band"></div>

  <div class="brand">
    <span class="brand-square"></span>
    <span class="brand-name">Harbor Peak Building Services</span>
  </div>

  <div class="letter-body issue-date">Issuing Date: May 5, 2018</div>

  <div class="letter-body recipient">
    Name Of Employee Mr. XYZABC<br>
    Address of Employee<br>
    Address Line 2 etc..
  </div>

  <div class="letter-body salutation">Dear Mr.XYZABC</div>

  <div class="letter-body paragraphs">
    <p>Lorem Ipsum has been the industry's standard dummy text ever since the 1500s, when an unknown printer took a galley of type and scrambled it to make a type specimen book. It has survived not only five centuries, but also the leap into electronic typesetting, remaining essentially unchanged. It was popularised in the 1960s with the release of Typeleaf sheets containing Lorem Ipsum passages, and more recently with desktop publishing software like Quillset Composer including versions of Lorem Ipsum.</p>
    <p>Lorem Ipsum is simply dummy text of the printing and typesetting industry. Lorem Ipsum has been the industry's standard dummy text ever since the 1500s, when an unknown printer took a galley of type and scrambled it to make a type specimen book.</p>
    <p>It has survived not only five centuries, but also the leap into electronic typesetting, remaining essentially unchanged. It was popularised in the 1960s with the release of Typeleaf sheets containing Lorem IpsumIpsum passages.</p>
  </div>

  <div class="letter-body closing">Yours Sincerely</div>

  <div class="letter-body signatory">
    <div class="signatory-name">Daniel Marsh</div>
    <div class="signatory-role">Managing Director</div>
  </div>

  <footer class="footer">
    <div class="footer-address">48 Kestrel Lane, Bayfield Victoria 3990</div>
    <div class="footer-rule"></div>
    <div class="footer-contacts">
      <span class="label">P:</span> 03 9000 4127<span class="sep">|</span><span class="label">E:</span> info@harborpeakbuilding.com.au<span class="sep">|</span>www.<span class="highlight">harborpeakbuilding</span>.com.au
    </div>
  </footer>
</div>
</body>
</html>
```